Wordpress Design Project

We are a Computer / Information Technology Company that will focus on the after-hours technical support for Home and Businesses.

I'm looking to have the home page as a static page with a links to blog, about us.

www.rkwidget.com.au is my web site.

Please do not chage uploaded logo's, do not copy current logo on website use uploaded files only, thanks.
Updates

Project Deadline Extended
Reason: No idea how this was posted with only 2 days!!

Cheers

Marcus

Project Deadline Extended
Reason: I have asked for some changes from designers.

Target Market(s)

Home and Small office/home office, or SOHO Computer users.

Industry/Entity Type

Computer

Requirements
Should not have
• After hours tech support added to logo.

```html
<!DOCTYPE html>
<html lang="en">
<head>
<meta charset="utf-8">
<title>RK Widget — Home</title>
<link rel="stylesheet" href="https://fonts.googleapis.com/css2?family=Noto+Sans:ital,wght@0,400;0,700;1,400&family=Arimo:ital,wght@0,400;1,400&display=swap">
<style>
:root{
  --header:#333333;
  --ink:#111111;
  --white:#ffffff;
  --accent:#22b4e6;
  --accent-soft:#7fd6f0;
  --hero-top:#82f1fb;
  --hero-bottom:#16c2e7;
  --footer:#000000;
  --nav-top:#f2f2f2;
  --nav-bottom:#2a2a2a;
}
*{margin:0;padding:0;box-sizing:border-box}
html,body{width:800px;height:1200px;overflow:hidden;background:var(--white)}
body{position:relative;font-family:"Noto Sans",Verdana,sans-serif;color:var(--ink)}
h2,h3{font-weight:400}
.abs{position:absolute}

.site-header{left:0;top:0;width:800px;height:116px;background:var(--header)}
.brand{left:30px;top:38px;display:flex;align-items:center;gap:14px;color:var(--accent);font-size:38px;font-weight:400;letter-spacing:1px}
.brand-dot{width:44px;height:44px;border-radius:50%;background:#8c8c8c}
.login-field{top:76px;width:79px;height:18px;background:var(--white);border-radius:5px;font-size:8px;text-align:center;line-height:18px;color:#222}
.login-links{right:9px;top:97px;color:var(--white);font-size:12px;word-spacing:3px}

.main-nav{left:0;top:116px;width:800px;height:38px;background:linear-gradient(var(--nav-top),#9a9a9a 45%,var(--nav-bottom))}
.nav-tab{top:124px;height:30px;font-family:Arimo,Arial,sans-serif;font-size:13px;color:var(--white);line-height:30px}
.nav-tab.is-active{left:22px;width:88px;background:var(--white);color:#333;text-align:center;border-radius:4px 4px 0 0}
.search-box{left:554px;top:122px;width:208px;height:26px;background:var(--white);border-radius:4px;font-family:Arimo,Arial,sans-serif;font-size:12.5px;line-height:26px;padding-left:21px}
.search-icon{left:767px;top:123px}

.hero{left:13px;top:156px;width:769px;height:327px;background:linear-gradient(var(--hero-top),var(--hero-bottom));box-shadow:3px 3px 4px rgba(0,0,0,.45)}
.hero-title{left:18px;top:284px;font-family:Arimo,Arial,sans-serif;font-style:italic;font-size:24px;color:var(--white)}
.hero-sub{left:172px;top:315px;font-family:Arimo,Arial,sans-serif;font-style:italic;font-size:15px;color:var(--white)}
.hero-image{left:404px;top:228px;width:336px;height:212px;background:linear-gradient(160deg,#1b7fd0,#0d3e78 60%,#1a1a1a);border-radius:6px}
.hero-arrow{top:314px}

.feature-title{top:530px;width:260px;text-align:center;font-size:20px;color:var(--accent)}
.feature-title.is-soft{color:var(--accent-soft)}
.feature-text{width:235px;font-size:9.4px;line-height:11.6px;text-align:justify;hyphens:auto;top:722px}
.read-more{top:870px;font-size:8px;color:var(--accent)}

.site-footer{left:0;top:942px;width:800px;height:258px;background:var(--footer);color:var(--white)}
.footer-title{top:960px;font-size:19px;color:var(--white)}
.footer-text{font-size:9.4px;line-height:11.6px;text-align:justify;hyphens:auto;color:var(--white)}
.post-title{left:554px;top:990px;font-size:17px;color:var(--accent)}
.post-meta{left:555px;top:1076px;font-size:7.5px;color:var(--accent);font-weight:700}
.bottom-links{left:382px;top:1170px;font-size:12.5px;color:var(--white);display:flex;gap:8px}
.bottom-links span+span{border-left:2px solid var(--white);padding-left:8px}
.social{top:1166px;width:22px;height:22px;border-radius:4px}
</style>
</head>
<body>

<header class="abs site-header"></header>
<div class="abs brand"><span class="brand-dot"></span>RK Widget</div>
<div class="abs login-field" style="left:618px">Username</div>
<div class="abs login-field" style="left:714px">Password</div>
<div class="abs login-links">Login&nbsp; Remember me&nbsp; Sign Up</div>

<nav class="abs main-nav"></nav>
<div class="abs nav-tab is-active">HOME</div>
<div class="abs nav-tab" style="left:144px">BLOG</div>
<div class="abs nav-tab" style="left:230px">CONTAC US</div>
<div class="abs nav-tab" style="left:370px">ABOUT US</div>
<div class="abs nav-tab" style="left:490px">NEWS</div>
<div class="abs search-box">Search ......</div>
<svg class="abs search-icon" width="26" height="26" viewBox="0 0 26 26"><circle cx="10" cy="10" r="7.5" fill="#e8f2f8" stroke="#9aa" stroke-width="2"/><line x1="15.5" y1="15.5" x2="23" y2="23" stroke="#888" stroke-width="3" stroke-linecap="round"/></svg>

<section class="abs hero"></section>
<div class="abs hero-title">“Technology in your hands”</div>
<div class="abs hero-sub">Make a life easy</div>
<div class="abs hero-image" role="img" aria-label="Open laptop with a blue screen"></div>
<svg class="abs hero-arrow" style="left:338px" width="32" height="32" viewBox="0 0 32 32"><circle cx="16" cy="16" r="16" fill="#5e9fae"/><path d="M20 9 L11 16 L20 23Z" fill="#fff"/></svg>
<svg class="abs hero-arrow" style="left:732px" width="32" height="32" viewBox="0 0 32 32"><circle cx="16" cy="16" r="16" fill="#5e9fae"/><path d="M12 9 L21 16 L12 23Z" fill="#fff"/></svg>

<h2 class="abs feature-title" style="left:12px">Reviews Product</h2>
<h2 class="abs feature-title" style="left:268px">Tips &amp; Tricks</h2>
<h2 class="abs feature-title is-soft" style="left:533px">Hardware</h2>

<div class="abs" style="left:32px;top:576px;width:224px;height:144px;background:linear-gradient(#5aa8e8,#dfeaf3)" role="img" aria-label="Laptop, tablet and phone showing a cloudy sky"></div>
<div class="abs" style="left:306px;top:583px;width:204px;height:135px;background:linear-gradient(135deg,#c9d3e0,#6f7c92)" role="img" aria-label="Hand plugging cables into a laptop"></div>
<div class="abs" style="left:567px;top:583px;width:197px;height:130px;background:radial-gradient(circle at 55% 45%,#d8d8d8,#3a3a3a 65%,#111)" role="img" aria-label="Open optical disc drive"></div>

<p class="abs feature-text" style="left:28px">Lorem Ipsum is simply dummy text of the printing and typesetting industry. Lorem Ipsum has been the industry's standard dummy text ever since the 1500s, when an unknown printer took a galley of type and scrambled it to make a type specimen book. It has survived not only five centuries, but also the leap into electronic typesetting, remaining essentially unchanged. It was popularised in the 1960s with the release of Letterwell sheets containing Lorem Ipsum passages,</p>
<p class="abs feature-text" style="left:290px">Lorem Ipsum is simply dummy text of the printing and typesetting industry. Lorem Ipsum has been the industry's standard dummy text ever since the 1500s, when an unknown printer took a galley of type and scrambled it to make a type specimen book. It has survived not only five centuries, but also the leap into electronic typesetting, remaining essentially unchanged. It was popularised in the 1960s with the release of Letterwell sheets containing Lorem Ipsum passages,</p>
<p class="abs feature-text" style="left:548px">Lorem Ipsum is simply dummy text of the printing and typesetting industry. Lorem Ipsum has been the industry's standard dummy text ever since the 1500s, when an unknown printer took a galley of type and scrambled it to make a type specimen book. It has survived not only five centuries, but also the leap into electronic typesetting, remaining essentially unchanged. It was popularised in the 1960s with the release of Letterwell sheets containing Lorem Ipsum passages,</p>
<a class="abs read-more" style="left:215px">Read More</a>
<a class="abs read-more" style="left:478px">Read More</a>
<a class="abs read-more" style="left:735px">Read More</a>

<footer class="abs site-footer"></footer>
<h3 class="abs footer-title" style="left:110px">News</h3>
<h3 class="abs footer-title" style="left:339px">e-Commerce</h3>
<h3 class="abs footer-title" style="left:555px">Blog</h3>

<div class="abs" style="left:74px;top:994px;width:119px;height:86px;background:linear-gradient(#ffffff,#d0d6dc)" role="img" aria-label="Laptop wearing a red holiday hat"></div>
<p class="abs footer-text" style="left:27px;top:1092px;width:221px">Lorem Ipsum is simply dummy text of the printing and typesetting industry. Lorem Ipsum has been the industry's standard dummy text ever since the 1500s, when an</p>
<a class="abs read-more" style="left:205px;top:1145px">Read More</a>

<p class="abs footer-text" style="left:292px;top:1012px;width:233px">Lorem Ipsum is simply dummy text of the printing and typesetting industry. Lorem Ipsum has been the industry's standard dummy text ever since the 1500s, when an unknown printer took a galley of type and scrambled it to make a type specimen book. It has survived not only five centuries, but also the leap into electronic typesetting, remaining essentially unchanged. It was popularised in the 1960s with the release of Letterwell sheets containing Lore</p>

<div class="abs post-title">Post Element</div>
<p class="abs footer-text" style="left:555px;top:1014px;width:235px">Lorem Ipsum is simply dummy text of the printing and typesetting industry. Lorem Ipsum has been the industry's standard dummy text ever since the 1500s, when an unknown printer took a galley of type and scrambled it to make a type</p>
<div class="abs post-meta">No Comment &nbsp;|&nbsp; Posted December 17<sup>th</sup></div>

<div class="abs bottom-links"><span>Copyright@2011</span><span>Abous Us</span><span>Contac Us</span><span>Blog</span></div>
<div class="abs social" style="left:691px;background:#f07a1a"></div>
<div class="abs social" style="left:720px;background:#f26a1b"></div>
<div class="abs social" style="left:749px;background:#3b5a9a"></div>
<div class="abs social" style="left:777px;background:#4aaee0"></div>

</body>
</html>
```